Halvor Interiors Studio New Business Card

I am opening a new division of my business. I am a high end interior designer, and the new business is writing specs for construction projects. It will be marketed to the VERY high end contractor, architects and realtors. The client will actually be the one who pays us and signs the agreement, but it will be the contractor, architect or realtor that will recommend us. I have attached my current card and our previous logo which is still used on some of our paperwork. I would like the new logo to be connected in some way to what we are currently using. We will need to have room on the card for a person's name. I'd like to omit the address as we might be moving the office soon. The web address is www.HalvorInteriorsStudio.example. For this design, please use my name, Marisol Fenwick.

Target Market(s)

High End Luxury Contractors, Realtors and Architects

Industry/Entity Type

Residential Construction

Contact Information for Business Card

Halvor Interiors Studio, Phone: 555-204-9167, www.HalvorInteriorsStudio.example , Marisol Fenwick

Font styles to use
Sans Serif

Colors
ec1f27

Requirements
Must have
• Some visual reference to my current card and logos. Use the colors submitted on the business card I attached.
Nice to have
• A visual reference to my current card and logos. Use the colors submitted on the card I attached.
Should not have
• A physical address

```html
<!DOCTYPE html>
<html lang="en">
<head>
<meta charset="utf-8">
<title>Halvor Interiors Studio – Business Card</title>
<link rel="stylesheet" href="https://fonts.googleapis.com/css2?family=Jost:wght@400;600&family=Open+Sans:wght@300;400&display=swap">
<style>
  :root {
    --page-bg: #ececec;
    --card-bg: #ffffff;
    --ink-name: #7a7a7a;
    --ink-tagline: #6a6a6a;
    --ink-strong: #5c5c5c;
    --ink-body: #555555;
    --band-top: #d5e9f6;
    --band-bottom: #e1eefa;
    --mark-blue: #bcdcf1;
  }
  * { box-sizing: border-box; margin: 0; padding: 0; }
  html, body {
    width: 1200px;
    height: 800px;
    overflow: hidden;
    background: var(--page-bg);
  }
  .canvas {
    position: relative;
    width: 1200px;
    height: 800px;
  }
  .business-card {
    position: absolute;
    left: 150px;
    top: 147px;
    width: 900px;
    height: 506px;
    background: var(--card-bg);
    box-shadow: 0 2px 6px rgba(0,0,0,0.08);
  }
  .brand-dot {
    position: absolute;
    left: 50%;
    top: 38px;
    width: 50px;
    height: 50px;
    margin-left: -25px;
    border-radius: 50%;
    background: var(--mark-blue);
  }
  .brand-name {
    position: absolute;
    left: 0;
    right: 0;
    top: 108px;
    text-align: center;
    font-family: "Jost", sans-serif;
    font-weight: 400;
    font-size: 60px;
    line-height: 1;
    color: var(--ink-name);
    letter-spacing: 0.5px;
  }
  .brand-tagline {
    position: absolute;
    left: 0;
    right: 0;
    top: 180px;
    text-align: center;
    font-family: "Open Sans", sans-serif;
    font-weight: 300;
    font-size: 18px;
    letter-spacing: 5.4px;
    color: var(--ink-tagline);
  }
  .contact-band {
    position: absolute;
    left: 58px;
    right: 58px;
    top: 250px;
    height: 212px;
    background: linear-gradient(180deg, var(--band-top), var(--band-bottom));
    text-align: center;
  }
  .company-name {
    margin-top: 40px;
    font-family: "Jost", sans-serif;
    font-weight: 600;
    font-size: 45px;
    letter-spacing: 1px;
    text-transform: uppercase;
    color: var(--ink-strong);
    line-height: 1.1;
  }
  .contact-line {
    font-family: "Open Sans", sans-serif;
    font-weight: 400;
    font-size: 24px;
    line-height: 35px;
    color: var(--ink-body);
  }
  .contact-line:first-of-type { margin-top: 8px; }
</style>
</head>
<body>
<main class="canvas">
  <section class="business-card">
    <div class="brand-dot"></div>
    <h1 class="brand-name">Marisol Fenwick</h1>
    <p class="brand-tagline">COMMERCIAL|RESIDENTIAL DESIGN</p>
    <div class="contact-band">
      <h2 class="company-name">Halvor Interiors Studio</h2>
      <p class="contact-line">Phone: 555-204-9167</p>
      <p class="contact-line">www.HalvorInteriorsStudio.example</p>
    </div>
  </section>
</main>
</body>
</html>
```